Flyer Design Project - Wine

We are an online fine and vintage wine merchant called The Heron's Larder (www.theheronslarder-example.com) we sell fine wine by the bottle, almost always at lower prices than everyone else, in elegant packaging and with next day delivery.

What we need is a leaflet to let people know what we do.

We're open to any size but like the idea of card folded twice to form 2 doors at the front. We have all logos, content and pictures ready to go and in high resolution. We would like a simple and classy design that will really get people opening and reading it.

CONTENT:

The Heron’s Larder is a boutique online fine and vintage wine merchant. So named as it was The Heron’s Larder that would hold the best wines in the land.

At The Heron’s Larder our objective is to make the exclusive more accessible and that is why you will notice our fine wine prices are lower than anywhere else especially once signed up to our loyalty program.

Unlike many wine merchants, we will not hesitate to crack open a case and sell you single bottles, but also have offers on full cases.

Fine wine deserves the best and all our bottles come in elegant packaging. They are wrapped in tissue, fastened with our wax seal, graced with tasting notes around the neck with the option of an elegant gift box.

We only want to sell you the best and this is why all our wines have high scores, usually in the high 80s and 90s, awarded by the world’s best critics and available for view on the wine’s profile.

As we seek extraordinary wines, naturally we have plenty of Bordeaux and Burgundy but we do stock exceptional new world wines too, focusing on winemakers who are renowned within the industry for quality and finesse.

Wines take time to reach their peak so we do our best to only offer wines that are aged and ready for drinking now, so you can enjoy them the moment they arrive but will note if they could be stored for longer. All our wines are kept in optimum conditions.

We offer next day delivery which is free in the UK for orders over £95 and perfect for that last minute gift or accompaniment to tomorrow’s dinner

On our site you will find all the information you need on each wine from tasting notes to background on the châteaux.

We guarantee the quality of our wine and will offer replacements should it not meet your expectations, unless stated otherwise.

If any questions remain unanswered we are always available to help.

www.theheronslarder-example.com
Updates

The design are all looking great the main points that need changing are:

More pictures of wine - I will be posting some more in a second, also we like having one picture of a wrapped bottle but not too many as we want people to buy for themselves too and not think that we are a gift company.

Simplified content and put in bold - The leaflets currently look like people wouldn't bother reading them or skimming them as the content is too dense. I know we wrote the content but if you could have a go at simplifying it and putting key lines in bold that would be great.

We don't want to include our address - we are online only.

We need a good deal of emphasis on our web address as it's the most important part of our business.

Liked:

The white backgrounds
The 2 door opening at the front
Square not rectangular shape
A creative and classy inside which makes you want to read it

Thank you all for your designs, they are really great and we look forward to the final product,

Martin

I''m going to put some more bottle photos up for those that need them.

As for the newer designs things to keep in mind are that we need this to be classy and quite consistent throughout (and with our website), so not too many different fonts and oddly shaped boxes.

Again the address really can''t be on there.

We don''t need a space for postage or any technical stamps.

We need less emphasis on the testimonials and more on that simplifies content.

We also need to add a bit to the content. Something along these lines:

"We guarantee the quality of our wine and will offer replacements should it not meet your expectations, unless stated otherwise."

Otherwise the designs are looking really great.

Industry/Entity Type

Boutique

Requirements
Must have
• -As an online only wine merchant getting our site name out there is very important. www.theheronslarder-example.com must be quite prominent on the leaflet.
-Pictures of our packaging

Nice to have
• -Simplicity
-The Heron's Larder logo looks good set against a white background.
-Some of the testimonials from our website
Should not have
• The address

```html
<!DOCTYPE html>
<html lang="en">
<head>
<meta charset="utf-8">
<title>The Heron’s Larder – Inside Spread</title>
<link rel="stylesheet" href="https://fonts.googleapis.com/css2?family=EB+Garamond:wght@400;600;700&family=Arimo:wght@400&display=swap">
<style>
  :root {
    --paper: #f4f4f3;
    --paper-shade: #e9e9e8;
    --fold: #b3b3b3;
    --ink: #1d1d1d;
    --wine-red: #b0161c;
    --frame: #8d8d8d;
    --frame-fill: #eeeeee;
    --ornament: #b9b9b9;
    --champagne: #d8c44a;
    --bottle-dark: #3a1012;
    --crate: #d9bf93;
  }
  html, body { margin: 0; padding: 0; overflow: hidden; }
  body { width: 1200px; height: 667px; background: #fff; }
  .spread {
    position: relative; width: 1200px; height: 667px; overflow: hidden;
    background: radial-gradient(ellipse at 50% 40%, var(--paper) 0%, var(--paper-shade) 100%);
    font-family: "EB Garamond", Garamond, serif; color: var(--ink);
  }
  .fold { position: absolute; top: 0; height: 667px; background: var(--fold); }
  .fold--left { left: 280px; width: 23px; }
  .fold--right { left: 870px; width: 22px; }

  /* Testimonials */
  .testimonial { position: absolute; left: 37px; width: 225px; text-align: center; }
  .testimonial__frame {
    border: 3px double var(--frame); background: var(--frame-fill);
    padding: 6px 8px; font-size: 15px; line-height: 19px;
    box-shadow: inset 0 0 0 2px #d4d4d4;
  }
  .testimonial__author {
    font-family: "Arimo", Arial, sans-serif; font-size: 11.5px;
    color: var(--wine-red); margin-top: 3px; letter-spacing: .3px;
  }
  .ornament { position: absolute; left: 90px; width: 116px; height: 30px;
    background: linear-gradient(90deg, transparent, var(--ornament) 30%, var(--ornament) 70%, transparent);
    border-radius: 15px; opacity: .7; }
  .pull-quote {
    position: absolute; left: 15px; top: 455px; width: 266px; text-align: center;
    color: var(--wine-red); font-weight: 700; font-size: 19.5px; line-height: 25px;
  }

  /* Centre panel */
  .centre-copy { position: absolute; left: 330px; width: 510px; text-align: center; font-size: 15.5px; line-height: 19.8px; margin: 0; }
  .centre-copy strong { color: var(--wine-red); }
  .brand { position: absolute; left: 490px; top: 245px; width: 190px; text-align: center; }
  .brand__mark { width: 70px; height: 70px; border-radius: 50%; background: var(--wine-red); margin: 0 auto 8px; }
  .brand__name { font-size: 17px; font-weight: 600; color: var(--wine-red); letter-spacing: 1px; }

  .photo { position: absolute; }
  .photo--champagne { left: 303px; top: 298px; width: 50px; height: 369px;
    background: linear-gradient(90deg, #b69d2c, var(--champagne) 50%, #a48a22); border-radius: 18px 18px 0 0; }
  .photo--claret { left: 812px; top: 300px; width: 58px; height: 367px;
    background: linear-gradient(90deg, #1f0708, var(--bottle-dark) 50%, #1a0506); border-radius: 20px 0 0 0; }
  .photo--case { left: 462px; top: 495px; width: 238px; height: 145px;
    background: linear-gradient(180deg, #efe6d6, var(--crate)); }
  .photo--bottles { left: 955px; top: 428px; width: 185px; height: 212px;
    background: linear-gradient(90deg, #2a1012, #3b1416 50%, #2a0c0d); border-radius: 30px 30px 4px 4px; }

  /* Right panel */
  .right-copy { position: absolute; left: 897px; width: 285px; font-size: 13.6px; line-height: 21px; text-align: justify; margin: 0; }
  .seal { position: absolute; left: 1015px; width: 38px; height: 38px; border-radius: 50%;
    background: radial-gradient(circle at 40% 40%, #d3262b, var(--wine-red) 70%); }
</style>
</head>
<body>
<main class="spread">
  <div class="fold fold--left"></div>
  <div class="fold fold--right"></div>

  <section class="panel panel--testimonials">
    <div class="testimonial" style="top:37px">
      <div class="testimonial__frame">Thank you very much.<br>Brilliant service. Ordered yesterday, delivered within 24 hours. A bottle will be drunk this weekend.</div>
      <div class="testimonial__author">D. S. (Bolton)</div>
    </div>
    <div class="testimonial" style="top:156px">
      <div class="testimonial__frame">Clear and easy with lots of wines on one page. I love the fact I can buy the odd, the old and the unusual.</div>
      <div class="testimonial__author">K. M. (Manchester)</div>
    </div>
    <div class="testimonial" style="top:264px">
      <div class="testimonial__frame">You are my favourite supplier of GOOD wine with some age that was drinking at time of purchase!"</div>
      <div class="testimonial__author">R. W. (London)</div>
    </div>
    <div class="ornament" style="top:406px" role="img" aria-label="Decorative scroll flourish"></div>
    <p class="pull-quote" style="margin:0">“At The Heron's Larder<br>our objective<br>is to make the exclusive<br>more accessible.”</p>
    <div class="ornament" style="top:570px" role="img" aria-label="Decorative scroll flourish"></div>
  </section>

  <section class="panel panel--centre">
    <p class="centre-copy" style="top:40px">The Heron’s Larder is a boutique online fine and<br>vintage wine merchant.So named as it was the heron’s larder<br>that would hold the best wines in the land.</p>
    <p class="centre-copy" style="top:120px">At The Heron’s Larder our objective is to make the exclusive<br>more accessible and that is why you will notice<br>our fine wine prices are lower than anywhere else especially<br>once <strong>signed up</strong> to our loyalty program.</p>
    <p class="centre-copy" style="top:208px">Unlike many wine merchants, we will not hesitate to crack<br>open a case and sell you single bottles, but also have offers on full cases.</p>
    <div class="brand">
      <div class="brand__mark"></div>
      <div class="brand__name">THE HERON’S LARDER</div>
    </div>
    <p class="centre-copy" style="top:378px;font-size:16.2px;line-height:22px">Fine wine deserves the best and all our bottles<br>come in elegant packaging.<br>They are wrapped in tissue, fastened with our<br>wax seal, graced with tasting notes<br>around the neck with the option of an elegant gift box.</p>
    <div class="photo photo--champagne" role="img" aria-label="Photo of a champagne bottle with gold label"></div>
    <div class="photo photo--claret" role="img" aria-label="Photo of a red Bordeaux bottle"></div>
    <div class="photo photo--case" role="img" aria-label="Photo of six tissue-wrapped bottles with red wax seals in a wooden case"></div>
  </section>

  <section class="panel panel--right">
    <p class="right-copy" style="top:5px">As we seek extraordinary wines, naturally we have plenty of Bordeaux and Burgundy but we do stock exceptional new world wines too, focusing on winemakers who are renowned within the industry for quality and finesse.</p>
    <div class="seal" style="top:146px"></div>
    <p class="right-copy" style="top:187px">Wines take time to reach their peak so we do our best to only offer wines that are aged and ready for drinking now, so you can enjoy them the moment they arrive but will note if they could be stored for longer. All our wines are kept in optimum conditions.</p>
    <div class="seal" style="top:299px"></div>
    <p class="right-copy" style="top:343px">We only want to sell you the best and this is why all our wines have high scores, usually in the high 80s and 90s, awarded by the world’s best critics and available for view on the wine’s profile.</p>
    <div class="photo photo--bottles" role="img" aria-label="Photo of four bottles of red wine and vintage port"></div>
  </section>
</main>
</body>
</html>
```